■ターゲット■
30~40代の主婦層

■制作する上での優先順位■
①サイトの見やすさ
②スマフォ最適化

■デザインのテイスト■
・モダン
・ナチュラル
・エレガント
・清潔な
・知性的

■希望デザインカラー
えんじ色 シルバー(ロゴがえんじ色です)

■サイトマップ■

1 TOP
2 コンセプト
3 会社概要
4 luminaのメニュー
5 luminaサロン情報
6 lumina tessaサロン情報
7 mirabel (フェイシャル&痩身)エステサロン サロン情報
8 hair produce lumina ~kagoshima ~ 港ヶ丘店
9 リクルート
10 プライバシー・ポリシー・お問い合わせ
11 mirabel(フェイシャル&痩身)エステサロン
12 mirabel (フェイシャル&痩身)エステサロン
13 覚えておきたいヘアケアアイテムの違い
14 luminaが提案する髪のお手入れ方法
15 ルミナで髪質改善されたお客様(一覧)
16 ルミナで髪質改善されたお客様(詳細)
17 ブログ・ニュース(一覧)
18 ブログ・ニュース(詳細)
19 サロンアイテム紹介(一覧)
20 サロンアイテム紹介(詳細)
http://www.tobirano-hairworks-demo.com
1ページ
赤系、グレー系
■素材について

①サロンの写真
枚数がありますので、下記よりダウンロードしてご使用ください。
http://filebako-demo.jp/download/7c2d90ab3318e46f0b5a71d9ce04b8f6a2c7135e
ダウンロードパスワード qm4rtx7b

また、現行サイトに掲載している写真や内容は今回のデザインの中にも
使用頂いてもちろん問題ありません。

②その他素材として必要なものがある場合には、ソラフォト画像をご使用ください。
その際、「定期契約」でダウンロード出来る画像のみを使用してください。
(画像検索した際に、出てくる、サムネイル下の画像番号の横にソラフォトのマークがあるものは使用しないようお願い致します)

ソラフォト以外の素材を使用する際には、必ず無料で提供いただける物のみご使用ください。
もう少し提案を見たい為、延長いたします。
是非ご提案よろしくおねがいします。

考えていたデザインに近かったため。

大変素敵なデザインばかりで悩みました。。
ご提案頂き有難うございます!
また機会がございましたらよろしくお願いいたします。

```html
<!DOCTYPE html>
<html lang="ja">
<head>
<meta charset="utf-8">
<title>hair produce lumina</title>
<link rel="stylesheet" href="https://fonts.googleapis.com/css2?family=Cormorant+Garamond:wght@400;500&family=Noto+Serif+JP:wght@300;400;500&display=swap">
<style>
:root{
  --wine:#b46a70;
  --wine-soft:#c48a8e;
  --ink:#333;
  --sub:#777;
  --line:#bbb;
  --bg:#fff;
}
*{margin:0;padding:0;box-sizing:border-box}
html,body{width:1200px;height:4452px;overflow:hidden;background:var(--bg)}
body{position:relative;font-family:"Noto Serif JP",serif;color:var(--ink)}
.abs{position:absolute}
.en{font-family:"Cormorant Garamond",serif;letter-spacing:.12em}
.photo{position:absolute}
/* header */
.site-header .brand-sub{left:36px;top:12px;font-size:10px;color:var(--ink);font-family:"Cormorant Garamond",serif}
.site-header .brand{left:36px;top:24px;font-size:22px;letter-spacing:.3em;font-family:"Cormorant Garamond",serif}
.global-nav{right:40px;top:36px;display:flex;gap:38px;font-size:11px}
/* hero */
.hero-logo{left:216px;top:236px;font-size:58px;letter-spacing:.35em;font-family:"Cormorant Garamond",serif;font-weight:500;line-height:1}
.hero-tag{left:556px;top:238px;font-size:13px;line-height:1.7}
.hero-tag span{font-family:"Cormorant Garamond",serif;font-size:16px;letter-spacing:.08em}
.scroll-label{left:72px;top:420px;font-size:11px;writing-mode:vertical-rl;letter-spacing:.2em;color:var(--sub)}
.scroll-label::after{content:"";display:block;width:1px;height:60px;background:var(--line);margin:10px auto 0}
/* section heads */
.sec-title{left:0;width:1200px;text-align:center;font-family:"Cormorant Garamond",serif;font-weight:400;font-size:30px;letter-spacing:.12em;color:#666}
.sec-title::after{content:"";display:block;width:40px;height:1px;background:var(--wine);margin:14px auto 0}
/* concept */
.block-wine{background:var(--wine-soft)}
.concept-head{left:448px;top:680px;width:512px;height:100px;background:#fff}
.concept-box{left:120px;top:1080px;width:980px;height:300px;background:#fff;box-shadow:0 0 0 1px #f0f0f0}
.concept-label{left:184px;top:1210px;font-size:14px;font-family:"Cormorant Garamond",serif;letter-spacing:.1em}
.concept-lead{left:184px;top:1252px;font-size:20px;letter-spacing:.12em}
.concept-body{left:636px;top:1130px;width:400px;font-size:12px;line-height:2.3;letter-spacing:.14em;color:var(--sub);font-family:"Cormorant Garamond",serif}
/* news */
.tabs{left:0;width:1200px;top:1612px;display:flex;justify-content:center;gap:36px;font-size:12px;font-family:"Cormorant Garamond",serif;letter-spacing:.1em}
.tabs .off{color:#aaa}
.tabs .on{border-bottom:1px solid var(--ink);padding-bottom:3px}
.card{position:absolute;width:232px}
.card .thumb{width:232px;height:120px}
.card .meta{display:flex;align-items:center;gap:12px;margin-top:14px;font-size:10px;color:var(--sub)}
.card .tag{background:var(--wine);color:#fff;padding:2px 10px;font-size:9px}
.card p{margin-top:10px;font-size:11px;line-height:1.9;letter-spacing:.08em;color:var(--sub);font-family:"Cormorant Garamond",serif}
.more{font-family:"Cormorant Garamond",serif;font-size:13px;display:flex;align-items:center;gap:12px;letter-spacing:.1em}
.more::after{content:"";width:70px;height:1px;background:var(--ink)}
/* feature band */
.feature{top:2332px;height:248px;width:400px}
.feature span{position:absolute;left:40px;top:40px;color:#fff;font-size:15px;line-height:1.7;letter-spacing:.06em}
/* shop */
.shop-caption{left:360px;top:3128px;font-size:9px;color:var(--sub);line-height:1.6}
.shop-info{left:720px;top:2872px;font-size:12px;line-height:2}
.btn{position:absolute;top:3016px;width:170px;height:36px;background:var(--wine);color:#fff;font-size:13px;display:flex;align-items:center;justify-content:center;letter-spacing:.06em}
/* items */
.item{position:absolute;width:200px;text-align:center}
.item .pic{width:100px;height:150px;margin:0 auto}
.item h3{margin-top:20px;font-family:"Cormorant Garamond",serif;font-weight:400;font-size:14px;letter-spacing:.1em}
.item p{font-size:9px;color:var(--sub);margin-top:4px}
/* recruit */
.recruit{left:0;top:4012px;width:1200px;height:240px;background:linear-gradient(90deg,#3a3a3a,#262626 50%,#3a3a3a)}
.recruit h2{position:absolute;left:208px;top:104px;color:#fff;font-family:"Cormorant Garamond",serif;font-weight:400;font-size:26px;letter-spacing:.14em}
.recruit p{position:absolute;left:420px;top:86px;width:560px;color:#ccc;font-size:11px;line-height:2.2;letter-spacing:.14em;font-family:"Cormorant Garamond",serif}
/* footer */
.foot-logo{left:0;width:1200px;top:4330px;text-align:center;font-family:"Cormorant Garamond",serif;font-size:26px;letter-spacing:.35em}
.copy{left:0;width:1200px;top:4384px;text-align:center;font-size:8px;color:var(--sub);letter-spacing:.1em}
.pagetop{left:1168px;top:4290px;writing-mode:vertical-rl;font-size:10px;letter-spacing:.2em;color:var(--sub)}
.pagetop::before{content:"";display:block;width:1px;height:60px;background:var(--line);margin:0 auto 10px}
</style>
</head>
<body>

<header class="site-header">
  <div class="abs brand-sub">hair produce lumina</div>
  <div class="abs brand">lumina</div>
  <nav class="abs global-nav en">
    <span>CONCEPT</span><span>MENU</span><span>NEWS/BLOG</span><span>STYLE</span><span>SHOP LIST</span><span>ITEM</span><span>COMPANY</span><span>CONTACT</span>
  </nav>
</header>

<section class="hero">
  <div class="abs hero-logo">lumina</div>
  <div class="abs hero-tag"><span>Produced by hair produce</span><br>〜ルミナ・港ヶ丘店で始めるすてきな毎日〜</div>
  <div class="photo" style="left:200px;top:292px;width:1000px;height:268px;background:linear-gradient(90deg,#3d4a66 0%,#7a3a30 30%,#b0483a 50%,#e8e6e2 70%,#6b7a9a 100%)" role="img" aria-label="夕暮れに照らされたサロンの外観"></div>
  <div class="abs scroll-label en">SCROLL</div>
</section>

<section class="concept">
  <div class="abs block-wine" style="left:928px;top:680px;width:272px;height:240px"></div>
  <div class="abs concept-head"></div>
  <h2 class="abs sec-title" style="top:712px">CONCEPT</h2>
  <div class="photo" style="left:64px;top:820px;width:1016px;height:280px;background:linear-gradient(90deg,#2a2a2a,#6a6a6a 40%,#3a3a3a 70%,#8a8a8a)" role="img" aria-label="サロン店内のセット面"></div>
  <div class="abs block-wine" style="left:1120px;top:1080px;width:80px;height:220px"></div>
  <div class="abs concept-box"></div>
  <div class="abs concept-label">CONCEPT</div>
  <div class="abs concept-lead">髪にも、お客様にも、優しい美容室</div>
  <p class="abs concept-body">Our salon offers calm care for your hair and daily life. We choose gentle products and careful methods so every guest can feel relaxed. Our stylists listen closely and plan a style that suits your lifestyle, your hair and your time. We hope you enjoy a quiet moment with us and leave feeling refreshed and beautiful every visit.</p>
</section>

<section class="news">
  <h2 class="abs sec-title" style="top:1508px">NEWS &amp; BLOG</h2>
  <div class="abs tabs"><span class="off">BLOG</span><span class="on">NEWS</span></div>

  <article class="card" style="left:64px;top:1692px"><div class="thumb" style="background:linear-gradient(135deg,#222,#777)" role="img" aria-label="サロン外観の写真"></div><div class="meta"><span>2017.09.01</span><span class="tag">NEWS</span></div><p>New autumn menu now open. Please book your visit early this season.</p></article>
  <article class="card" style="left:344px;top:1692px"><div class="thumb" style="background:linear-gradient(135deg,#999,#333)" role="img" aria-label="店内の写真"></div><div class="meta"><span>2017.08.24</span><span class="tag">NEWS</span></div><p>Holiday hours notice for the coming week. Thank you for your support.</p></article>
  <article class="card" style="left:620px;top:1692px"><div class="thumb" style="background:linear-gradient(135deg,#444,#bbb)" role="img" aria-label="店内の写真"></div><div class="meta"><span>2017.08.10</span><span class="tag">NEWS</span></div><p>Our new care item has arrived. Ask our staff for details in the salon.</p></article>
  <article class="card" style="left:896px;top:1692px"><div class="thumb" style="background:linear-gradient(135deg,#ccc,#555)" role="img" aria-label="店内の写真"></div><div class="meta"><span>2017.07.30</span><span class="tag">NEWS</span></div><p>Summer campaign for hair treatment. Enjoy soft and healthy hair now.</p></article>

  <article class="card" style="left:64px;top:1952px"><div class="thumb" style="background:linear-gradient(135deg,#333,#888)" role="img" aria-label="店内の写真"></div><div class="meta"><span>2017.07.12</span><span class="tag">NEWS</span></div><p>Recruiting new stylists. Join our friendly team and grow with us.</p></article>
  <article class="card" style="left:344px;top:1952px"><div class="thumb" style="background:linear-gradient(135deg,#aaa,#222)" role="img" aria-label="店内の写真"></div><div class="meta"><span>2017.06.28</span><span class="tag">NEWS</span></div><p>Rainy season hair tips from our team. Keep your style all day long.</p></article>
  <article class="card" style="left:620px;top:1952px"><div class="thumb" style="background:linear-gradient(135deg,#1e1e1e,#666)" role="img" aria-label="サロン入口の写真"></div><div class="meta"><span>2017.06.15</span><span class="tag">NEWS</span></div><p>Esthetic menu update for facial care. Book online or by phone today.</p></article>
  <article class="card" style="left:896px;top:1952px"><div class="thumb" style="background:linear-gradient(135deg,#777,#ddd)" role="img" aria-label="店内の写真"></div><div class="meta"><span>2017.06.01</span><span class="tag">NEWS</span></div><p>Thank you for ten years. A small gift awaits every guest this month.</p></article>

  <div class="abs more" style="left:560px;top:2204px">More</div>
</section>

<section class="features">
  <div class="photo feature" style="left:0;background:linear-gradient(135deg,#9a9a9a,#5a5a5a)" role="img" aria-label="ヘアケアを受ける女性の写真"><span>lumina が提案する髪の<br>お手入れ方法</span></div>
  <div class="photo feature" style="left:400px;background:linear-gradient(135deg,#3a3a3a,#7a7a7a)" role="img" aria-label="ヘアケアアイテムのボトルの写真"><span>覚えておきたい<br>ヘアケアアイテムの違い</span></div>
  <div class="photo feature" style="left:800px;background:linear-gradient(135deg,#bdbdbd,#6a6a6a)" role="img" aria-label="髪を整える女性の写真"><span>ルミナで髪質改善<br>されたお客様</span></div>
</section>

<section class="shop">
  <h2 class="abs sec-title" style="top:2668px">SHOP LIST</h2>
  <div class="photo" style="left:64px;top:2792px;width:520px;height:328px;background:linear-gradient(180deg,#2c4a7a 0%,#4a6aa0 40%,#a8452f 60%,#e8e4de 80%,#555 100%)" role="img" aria-label="サロン外観の写真"></div>
  <div class="abs shop-caption">hair produce lumina<br>港ヶ丘店</div>
  <div class="abs shop-info">lumina ~本店<br>TEL：000-0000-0000（受付時間）<br>住所：〒000-0000 港ヶ丘市○○町0-0-0</div>
  <div class="btn" style="left:720px">Socialbook</div>
  <div class="btn" style="left:912px">Salon info</div>
  <div class="photo" style="left:1112px;top:2792px;width:88px;height:328px;background:linear-gradient(180deg,#3a3a3a,#8a8a8a)" role="img" aria-label="別店舗の外観写真"></div>
</section>

<section class="items">
  <h2 class="abs sec-title" style="top:3236px">ITEM LINEUP</h2>
  <div class="item" style="left:100px;top:3350px"><div class="pic" style="background:linear-gradient(180deg,#e8dcc4,#5a3a24)" role="img" aria-label="ヘアケア商品の写真"></div><h3>RECRUIT</h3><p>ヘアケアアイテム</p></div>
  <div class="item" style="left:370px;top:3350px"><div class="pic" style="background:linear-gradient(180deg,#e8dcc4,#5a3a24)" role="img" aria-label="ヘアケア商品の写真"></div><h3>RECRUIT</h3><p>ヘアケアアイテム</p></div>
  <div class="item" style="left:640px;top:3350px"><div class="pic" style="background:linear-gradient(180deg,#d8d0e0,#4a3a5a)" role="img" aria-label="シャンプーボトルの写真"></div><h3>RECRUIT</h3><p>ヘアケアアイテム</p></div>
  <div class="item" style="left:910px;top:3350px"><div class="pic" style="background:linear-gradient(180deg,#d8d0e0,#4a3a5a)" role="img" aria-label="シャンプーボトルの写真"></div><h3>RECRUIT</h3><p>ヘアケアアイテム</p></div>
  <div class="item" style="left:100px;top:3590px"><div class="pic" style="background:linear-gradient(180deg,#e8dcc4,#5a3a24)" role="img" aria-label="ヘアケア商品の写真"></div><h3>RECRUIT</h3><p>ヘアケアアイテム</p></div>
  <div class="item" style="left:370px;top:3590px"><div class="pic" style="background:linear-gradient(180deg,#e8dcc4,#5a3a24)" role="img" aria-label="ヘアケア商品の写真"></div><h3>RECRUIT</h3><p>ヘアケアアイテム</p></div>
  <div class="item" style="left:640px;top:3590px"><div class="pic" style="background:linear-gradient(180deg,#d8d0e0,#3a3a3a)" role="img" aria-label="シャンプーボトルの写真"></div><h3>RECRUIT</h3><p>ヘアケアアイテム</p></div>
  <div class="item" style="left:910px;top:3590px"><div class="pic" style="background:linear-gradient(180deg,#d8d0e0,#3a3a3a)" role="img" aria-label="シャンプーボトルの写真"></div><h3>RECRUIT</h3><p>ヘアケアアイテム</p></div>
  <div class="abs more" style="left:560px;top:3890px">More</div>
</section>

<section class="abs recruit" role="img" aria-label="サロン店内を背景にした採用案内">
  <h2>RECRUIT</h2>
  <p>We are looking for new team members who love hair and people. Grow your skills with us in a warm and calm salon, and build a career you can be proud of.</p>
</section>

<footer>
  <div class="abs foot-logo">lumina</div>
  <div class="abs copy">© hair produce lumina All rights reserved.</div>
  <div class="abs pagetop en">PAGE TOP</div>
</footer>

</body>
</html>
```